Paddock Guard Solutions Business Cards and Logo

I am commencing a niche safety business for horse racing stables and breeders. The registered business name is 'Paddock Guard Solutions'. It is a business of TOVEN Advisory. The page on my website www.tovenadvisory.com.au outlines the services offered.

The most important aspect is the development of a simple logo. I envisage a logo something like three horse heads in a simple outline to form the letter E for Paddock Guard Solutions. Alternatively a simple line drawing of a horse head that might be used on stationery and merchandise for example, a logo that might be used on a polo shirt and bumber stickers.

Industry/Entity Type

Business

Contact Information for Business Card

Martin Keble
Director
Paddock Guard Solutions
'Good stables are safe stables'
A business of TOVEN Advisory
0491 738 205
martin@tovenadvisory.com.au
www.tovenadvisory.com.au

Requirements
Must have
• Logo (see above)
Name: Martin Keble
Title: Director
Business Name: Paddock Guard Solutions
Motto: 'Good stables are safe stables'
A business of TOVEN Advisory (smaller print and probably ilalicised)
Phone: 0491 738 205
Email: martin@tovenadvisory.com.au
Web Address: www.tovenadvisory.com.au

```html
<!DOCTYPE html>
<html lang="en">
<head>
<meta charset="utf-8">
<title>Paddock Guard Solutions – Business Cards</title>
<link rel="stylesheet" href="https://fonts.googleapis.com/css2?family=Marcellus&family=Open+Sans:ital,wght@0,400;0,600;1,400&display=swap">
<style>
  :root {
    --backdrop: #2a2a2a;
    --brand-red: #e41e31;
    --ice-blue: #a9def0;
    --paper: #ffffff;
    --card-w: 520px;
    --card-h: 297px;
  }
  * { box-sizing: border-box; margin: 0; padding: 0; }
  html, body {
    width: 1200px; height: 809px; overflow: hidden;
    background: var(--backdrop);
    font-family: "Open Sans", Arial, sans-serif;
  }
  .stage { position: relative; width: 1200px; height: 809px; }

  .card {
    position: absolute;
    width: var(--card-w); height: var(--card-h);
    overflow: hidden;
    box-shadow: 0 6px 18px rgba(0,0,0,.45);
  }

  /* Front */
  .card--front {
    left: 60px; top: 110px;
    background: var(--brand-red);
    padding: 64px 40px 0 46px;
  }
  .brand-name {
    font-family: "Marcellus", Georgia, serif;
    color: var(--ice-blue);
    font-size: 34px;
    line-height: 1.1;
    letter-spacing: .5px;
    white-space: nowrap;
  }
  .brand-parent {
    margin-top: 6px;
    font-style: italic;
    font-size: 11px;
    color: var(--ice-blue);
  }
  .card--front .tagline {
    margin-top: 26px;
    font-style: italic;
    font-size: 21px;
    color: var(--ice-blue);
  }

  /* Back */
  .card--back {
    left: 620px; top: 400px;
    background: var(--paper);
  }
  .back-band {
    height: 140px;
    background: var(--brand-red);
    padding: 36px 30px 0 34px;
  }
  .back-band .brand-name { font-size: 30px; }
  .back-band .brand-parent { font-size: 10px; }

  .contact {
    position: absolute; left: 30px; right: 26px; bottom: 16px;
  }
  .contact-name {
    text-align: right;
    font-weight: 600; font-size: 20px; line-height: 1.3; color: var(--brand-red);
  }
  .contact-role {
    text-align: right;
    font-size: 14px; line-height: 1.3; color: var(--ice-blue);
  }
  .contact-row {
    display: flex; justify-content: space-between; align-items: center;
    margin-top: 4px;
  }
  .contact-line {
    display: flex; align-items: center; gap: 6px;
    font-size: 15px; color: var(--brand-red); line-height: 1.6;
    white-space: nowrap;
  }
  .contact-line svg { width: 15px; height: 15px; flex: none; }
  .contact-line--web { font-size: 16px; }
</style>
</head>
<body>
<main class="stage">

  <section class="card card--front" aria-label="Business card front">
    <h1 class="brand-name">Paddock Guard Solutions</h1>
    <p class="brand-parent">A Business of TOVEN Advisory</p>
    <p class="tagline">“Good stables are safe stables”</p>
  </section>

  <section class="card card--back" aria-label="Business card back">
    <div class="back-band">
      <h2 class="brand-name">Paddock Guard Solutions</h2>
      <p class="brand-parent">A business of TOVEN Advisory</p>
    </div>

    <div class="contact">
      <p class="contact-name">Martin Keble</p>
      <p class="contact-role">Director</p>
      <div class="contact-row">
        <p class="contact-line">
          <svg viewBox="0 0 16 16" aria-hidden="true"><rect x="1" y="3" width="14" height="10" fill="var(--ice-blue)"/><path d="M1 3l7 6 7-6" fill="none" stroke="#fff" stroke-width="1.2"/></svg>
          martin@tovenadvisory.com.au
        </p>
        <p class="contact-line">
          <svg viewBox="0 0 16 16" aria-hidden="true"><path d="M4 1.5l2.2 3-1.3 1.6c.9 2 2.4 3.5 4.4 4.4l1.6-1.3 3 2.2-1.2 2.6C7 14 2 9 1.4 2.7z" fill="var(--ice-blue)"/></svg>
          0491 738 205
        </p>
      </div>
      <p class="contact-line contact-line--web">
        <svg viewBox="0 0 16 16" aria-hidden="true"><circle cx="8" cy="8" r="6.5" fill="none" stroke="var(--ice-blue)" stroke-width="1.5"/><path d="M1.5 8h13M8 1.5c-3 3.5-3 9.5 0 13M8 1.5c3 3.5 3 9.5 0 13" fill="none" stroke="var(--ice-blue)" stroke-width="1.1"/></svg>
        www.tovenadvisory.com.au
      </p>
    </div>
  </section>

</main>
</body>
</html>
```